Zandrix fresh re-design

We are UK based company and have Magento website which we are happy with, but we require fresh design. Menu must be customer friendly

Design must reflect in strength as strength of our products and value for money are our selling points.

Our products are not family products there mainly used for business at events, cycling, running clubs, etc

New design must have same information as current design

links that require new design

http://www.zandrix.example (landing page)

http://www.zandrix.example/3m-x-3m-heavy-duty-tents/3m-x-3m-pop-up-marquee-white.html (product page)

http://www.zandrix.example/custom-design-own-tent-size/choose-3mx3m.html (design tool)

Target Market(s)

business owners, cycling clubs, running clubs,

Industry/Entity Type

It Company

Number of Pages Required

3 page

Requirements
Must have
• background image of working poptent, clean fresh design, printed zandrix eg. cupcake
Should not have
• all same functions as current page

```html
<!DOCTYPE html>
<html lang="en">
<head>
<meta charset="utf-8">
<title>Zandrix – Heavy Duty Pop-up Tents</title>
<link href="https://fonts.googleapis.com/css2?family=Open+Sans:wght@400;600;700;800&display=swap" rel="stylesheet">
<style>
:root{
  --red:#ee3a3b;
  --blue:#2446c8;
  --green:#4fa33a;
  --yellow:#f5c518;
  --ink:#333;
  --muted:#666;
  --grey-text:#555;
  --line:#cfcfcf;
  --footer:#f1f1f1;
  --sw-blue:#1d4fb0;
  --sw-orange:#f07a1c;
  --sw-green:#2fae3a;
  --sw-red:#ee2a1b;
}
*{box-sizing:border-box;margin:0;padding:0}
html,body{width:1200px;height:2799px;overflow:hidden;background:#fff}
body{position:relative;font-family:"Open Sans",Arial,sans-serif;color:var(--ink)}
a{color:inherit;text-decoration:none}
.abs{position:absolute}

/* header */
.utility{top:12px;right:75px;font-size:11px;display:flex;gap:10px;align-items:center;color:var(--red)}
.utility .welcome{color:#333}
.utility .cart{width:18px;height:14px}
.brand{top:58px;left:75px;display:flex;align-items:center;gap:10px;font-size:34px;font-weight:700;color:var(--red);letter-spacing:-.5px}
.brand .mark{width:22px;height:22px;background:var(--red)}
.contact-line{top:74px;right:75px;font-size:12px;color:#555;display:flex;gap:10px;align-items:center}
.contact-line svg{width:12px;height:12px}
.main-nav{top:144px;left:75px;right:75px;display:flex;justify-content:space-between;font-size:13px;letter-spacing:1.2px;color:#666;text-transform:uppercase}
.main-nav .active{color:var(--red)}
.main-nav .caret{font-size:9px;margin-left:3px}

/* hero */
.hero{top:193px;left:0;width:1200px;height:493px;overflow:hidden;background:linear-gradient(135deg,#3a3550 0%,#7b6f86 40%,#5a4c6a 70%,#2d2838 100%)}
.hero-photo{position:absolute;inset:0;background:
  linear-gradient(180deg,transparent 0,transparent 60%,rgba(0,0,0,.15) 100%),
  linear-gradient(90deg,transparent 0,transparent 6%,#3e49d6 6%,#2a35c8 36%,transparent 36%),
  linear-gradient(90deg,transparent 0,transparent 36%,#f2a714 36%,#e9a010 55%,transparent 55%);
  background-size:100% 100%,100% 100%,100% 100%;
  clip-path:polygon(6% 16%,36% 16%,36% 40%,55% 40%,55% 84%,36% 84%,36% 58%,6% 58%);opacity:.9}
.hero-weight{position:absolute;right:0;top:190px;width:150px;height:170px;border-radius:50% 0 0 50%;background:#e8d21a}
.hero-stripes{position:absolute;left:0;top:248px;width:1200px}
.hero-stripes i{display:block;height:6px;margin-bottom:8px;background:#fff}
.hero-stripes i.d{background:#1b1b26}
.tagline{position:absolute;left:660px;top:190px;text-align:left;font-weight:800;line-height:1;letter-spacing:-1px}
.tagline .t1{display:block;font-size:38px;color:var(--red);margin-left:64px}
.tagline .t2{display:block;font-size:78px;color:var(--red);margin-top:2px}
.tagline .t3{display:block;font-size:72px;color:var(--blue);margin-left:88px;margin-top:-2px}
.tagline span{text-shadow:0 0 0 transparent}
.hero-dots{top:214px;left:562px;display:flex;gap:10px}
.hero-dots span{width:16px;height:16px;border-radius:50%;background:#2f5bd1}
.hero-dots span.on{background:var(--red)}

/* promos */
.promo-custom{top:725px;left:75px;width:693px;height:191px;border:1px solid var(--line);background:#fff}
.promo-custom .pic{position:absolute;left:10px;top:6px;width:350px;height:178px;background:linear-gradient(90deg,#9c1b2c 0%,#9c1b2c 40%,#3f9a35 60%,#55b847 100%)}
.promo-custom .copy{position:absolute;right:24px;top:10px;text-align:right;line-height:1.2}
.promo-custom .l1{font-size:26px;color:var(--red);font-weight:600}
.promo-custom .l2{font-size:33px;color:var(--green);font-weight:600}
.promo-custom .l3{font-size:33px;color:var(--red);font-weight:600}
.btn{display:inline-block;background:var(--red);color:#fff;font-weight:600;text-align:center}
.promo-custom .btn{margin-top:10px;font-size:24px;padding:2px 22px}
.promo-why{top:725px;left:791px;width:334px;height:191px;background:var(--red);color:#fff;text-align:center;padding-top:16px;line-height:1.3}
.promo-why .h{font-size:30px;font-weight:700}
.promo-why .s{font-size:24px;font-weight:600}
.promo-why .y{font-size:24px;color:var(--yellow);font-weight:600}
.promo-why .btn{background:var(--yellow);color:var(--red);font-size:22px;padding:2px 30px;margin-top:6px}

/* features */
.feature{top:950px;width:336px;height:90px;border:2px solid var(--line);display:flex;align-items:center;justify-content:center;gap:18px;color:var(--red);font-size:24px;font-weight:600}
.feature svg{width:46px;height:46px}

/* products */
.section-title{top:1062px;left:0;width:1200px;text-align:center;font-size:30px;font-weight:700;color:var(--red)}
.product{width:248px;text-align:center}
.product .pic{height:237px}
.pic.blue{background:linear-gradient(180deg,#8ec4ee 0%,#1f4fd6 30%,#1d3fb8 75%,#4e6b2e 100%)}
.pic.orange{background:linear-gradient(180deg,#f09a33 0%,#f36d10 35%,#e45d08 75%,#5a6a34 100%)}
.pic.white{background:linear-gradient(180deg,#2d3a2a 0%,#e9e9e9 20%,#d8d8d6 70%,#4f7a33 100%)}
.pic.cupcake{background:linear-gradient(180deg,#2a3a24 0%,#f3c7da 20%,#e8eaf3 45%,#4f8a31 65%,#3e7a28 100%)}
.product .name{margin-top:16px;font-size:18px;line-height:24px;color:var(--muted);font-weight:400}
.product .price{margin-top:8px;font-size:32px;font-weight:700;color:#666}
.swatches{margin-top:6px;display:flex;justify-content:center;gap:6px}
.swatches i{width:16px;height:16px;display:block}
.swatches .b{background:var(--sw-blue)}.swatches .o{background:var(--sw-orange)}.swatches .g{background:var(--sw-green)}.swatches .w{background:#fff;border:2px solid #111}.swatches .r{background:var(--sw-red)}
.product .btn{display:block;margin-top:12px;height:34px;line-height:34px;font-size:22px;font-weight:400}

/* partners */
.partners{top:2196px;left:75px;right:75px;display:flex;justify-content:space-between;align-items:center;font-size:20px;font-weight:700;color:#222}
.partners span{display:flex;align-items:center;gap:8px}
.partners i{width:16px;height:16px;background:var(--red);display:block}
.partner-dots{top:2262px;left:597px;display:flex;gap:12px}
.partner-dots span{width:7px;height:7px;border-radius:50%;background:#aaa}
.partner-dots span.on{background:var(--red)}

/* footer */
.site-footer{top:2313px;left:0;width:1200px;height:368px;background:var(--footer)}
.footer-col{top:2354px;font-size:16px;line-height:28px;color:var(--grey-text)}
.footer-col h3{font-size:22px;color:var(--red);font-weight:700;margin-bottom:8px;line-height:30px}
.footer-col b{font-weight:700;color:#444}
.newsletter-input{top:2520px;left:796px;width:220px}
.newsletter-input .label{font-size:15px;color:#555;margin-bottom:10px;padding-left:6px}
.newsletter-input .field{height:40px;background:#e2e2e2}
.newsletter-input .btn{display:block;margin-top:10px;height:40px;line-height:40px;font-size:22px;font-weight:400}

.bottom-bar{top:2681px;left:0;width:1200px;height:118px;background:#ffffff;z-index:1}
.bottom-brand,.social,.cards,.copyright{z-index:2}
.bottom-brand{top:2712px;left:75px;display:flex;align-items:center;gap:8px;font-size:22px;font-weight:700;color:var(--red)}
.bottom-brand .mark{width:14px;height:14px;background:var(--red)}
.social{top:2717px;left:254px;display:flex;gap:6px}
.social i,.cards i{display:block;background:var(--red)}
.social i{width:22px;height:22px;border-radius:3px}
.cards{top:2714px;left:414px;display:flex;gap:8px}
.cards i{width:46px;height:30px;border-radius:3px}
.copyright{top:2720px;left:676px;font-size:14px;color:var(--red)}
</style>
</head>
<body>

<header>
  <nav class="abs utility">
    <span class="welcome">WELCOME MESSAGE!</span><span>|</span>
    <a href="#">MY ACCOUNT</a><span>|</span>
    <a href="#">DAILY DEAL</a><span>|</span>
    <a href="#">MY WISHLIST</a><span>|</span>
    <a href="#">BLOG</a><span>|</span>
    <a href="#">LOG IN</a>
    <svg class="cart" viewBox="0 0 18 14" aria-label="Cart"><path d="M0 1h3l2 8h10l2-6H5" fill="none" stroke="#ee3a3b" stroke-width="1.8"/><circle cx="7" cy="12" r="1.5" fill="#ee3a3b"/><circle cx="14" cy="12" r="1.5" fill="#ee3a3b"/></svg>
  </nav>
  <div class="abs brand"><span class="mark"></span>zandrix.eu</div>
  <div class="abs contact-line">
    <svg viewBox="0 0 12 12"><path d="M2 1l2 0 1 3-1.5 1a7 7 0 0 0 3.5 3.5L8 7l3 1v2a1 1 0 0 1-1 1A9 9 0 0 1 1 2a1 1 0 0 1 1-1z" fill="#777"/></svg>
    <span>+44 20 7946 0311</span><span>|</span><span>CONTACT US</span>
  </div>
  <nav class="abs main-nav">
    <a class="active" href="#">Home</a>
    <a href="#">Product list<span class="caret">▼</span></a>
    <a href="#">Zandrix</a>
    <a href="#">Roofs</a>
    <a href="#">Walls</a>
    <a href="#">Gazebo weights</a>
    <a href="#">Gutters</a>
    <a href="#">Sandbags</a>
    <a href="#">Tables</a>
    <a href="#">Parts</a>
  </nav>
</header>

<section class="abs hero">
  <div class="hero-photo" role="img" aria-label="Blue and yellow pop-up tents set up under a steel frame"></div>
  <div class="hero-weight" role="img" aria-label="Yellow tent leg weight"></div>
  <div class="hero-stripes"><i></i><i class="d"></i><i></i></div>
  <h1 class="tagline"><span class="t1">World's</span><span class="t2">Strongest</span><span class="t3">Zandrix</span></h1>
</section>
<div class="abs hero-dots"><span></span><span class="on"></span><span></span></div>

<section class="abs promo-custom">
  <div class="pic" role="img" aria-label="Red and green custom printed pop-up tents"></div>
  <div class="copy">
    <div class="l1">Design Your Own</div>
    <div class="l2">Custom Zandrix</div>
    <div class="l3">From €490</div>
    <a class="btn" href="#">Order now!</a>
  </div>
</section>
<section class="abs promo-why">
  <div class="h">Why Buy From Us?</div>
  <div class="s">Zandrix provides</div>
  <div class="y">The cheapest prices</div>
  <a class="btn" href="#">Learn More</a>
</section>

<div class="abs feature" style="left:75px">
  <svg viewBox="0 0 46 46"><circle cx="23" cy="17" r="9" fill="#ee3a3b"/><path d="M8 44c0-10 7-16 15-16s15 6 15 16z" fill="#ee3a3b"/><path d="M11 19a12 12 0 0 1 24 0" fill="none" stroke="#ee3a3b" stroke-width="3"/><rect x="8" y="16" width="5" height="9" rx="2" fill="#ee3a3b"/><rect x="33" y="16" width="5" height="9" rx="2" fill="#ee3a3b"/></svg>
  Expert Advice
</div>
<div class="abs feature" style="left:432px">
  <svg viewBox="0 0 46 46"><path d="M23 3l17 6v12c0 11-8 19-17 22C14 40 6 32 6 21V9z" fill="#ee3a3b"/><path d="M15 23l6 6 11-12" fill="none" stroke="#fff" stroke-width="4"/></svg>
  Secure Shopping
</div>
<div class="abs feature" style="left:791px">
  <svg viewBox="0 0 60 46" style="width:60px"><rect x="14" y="10" width="28" height="22" fill="#ee3a3b"/><path d="M42 16h9l7 8v8H42z" fill="#ee3a3b"/><circle cx="22" cy="35" r="5" fill="#ee3a3b" stroke="#fff" stroke-width="2"/><circle cx="50" cy="35" r="5" fill="#ee3a3b" stroke="#fff" stroke-width="2"/><path d="M2 16h9M4 22h9M6 28h7" stroke="#ee3a3b" stroke-width="2.5"/></svg>
  Free Fast Delivery
</div>

<h2 class="abs section-title">OUR PRODUCTS</h2>

<article class="abs product" style="top:1128px;left:75px"><div class="pic blue" role="img" aria-label="Blue 3x3m heavy duty pop-up tent on grass"></div><h3 class="name">3mx3m Heavy Duty<br>Pop up White</h3><div class="price">€449</div><div class="swatches"><i class="b"></i><i class="o"></i><i class="g"></i><i class="w"></i><i class="r"></i></div><a class="btn" href="#">Add to cart</a></article>
<article class="abs product" style="top:1128px;left:342px"><div class="pic orange" role="img" aria-label="Orange 3x3m pop-up tent with walls"></div><h3 class="name">3mx3m Pop up<br>Extreme Orange</h3><div class="price">€449</div><div class="swatches"><i class="b"></i><i class="o"></i><i class="g"></i><i class="w"></i><i class="r"></i></div><a class="btn" href="#">Add to cart</a></article>
<article class="abs product" style="top:1128px;left:611px"><div class="pic white" role="img" aria-label="White 3x4.5m heavy duty pop-up tent on grass"></div><h3 class="name">3mx4.5m Heavy Duty<br>Pop up White</h3><div class="price">€549</div><div class="swatches"><i class="b"></i><i class="o"></i><i class="g"></i><i class="w"></i><i class="r"></i></div><a class="btn" href="#">Add to cart</a></article>
<article class="abs product" style="top:1128px;left:879px"><div class="pic cupcake" role="img" aria-label="3x3m party tent with printed cupcake roof on grass"></div><h3 class="name">3mx3m Cupcake<br>Party</h3><div class="price">€149</div><div class="swatches"><i class="b"></i><i class="o"></i><i class="g"></i><i class="w"></i><i class="r"></i></div><a class="btn" href="#">Add to cart</a></article>

<article class="abs product" style="top:1627px;left:75px"><div class="pic blue" role="img" aria-label="Blue 3x3m heavy duty pop-up tent on grass"></div><h3 class="name">3mx3m Heavy Duty<br>Pop up White</h3><div class="price">€449</div><div class="swatches"><i class="b"></i><i class="o"></i><i class="g"></i><i class="w"></i><i class="r"></i></div><a class="btn" href="#">Add to cart</a></article>
<article class="abs product" style="top:1627px;left:342px"><div class="pic orange" role="img" aria-label="Orange 3x3m pop-up tent with walls"></div><h3 class="name">3mx3m Pop up<br>Extreme Orange</h3><div class="price">€449</div><div class="swatches"><i class="b"></i><i class="o"></i><i class="g"></i><i class="w"></i><i class="r"></i></div><a class="btn" href="#">Add to cart</a></article>
<article class="abs product" style="top:1627px;left:611px"><div class="pic white" role="img" aria-label="White 3x4.5m heavy duty pop-up tent on grass"></div><h3 class="name">3mx4.5m Heavy Duty<br>Pop up White</h3><div class="price">€549</div><div class="swatches"><i class="b"></i><i class="o"></i><i class="g"></i><i class="w"></i><i class="r"></i></div><a class="btn" href="#">Add to cart</a></article>
<article class="abs product" style="top:1627px;left:879px"><div class="pic cupcake" role="img" aria-label="3x3m party tent with printed cupcake roof on grass"></div><h3 class="name">3mx3m Cupcake<br>Party</h3><div class="price">€149</div><div class="swatches"><i class="b"></i><i class="o"></i><i class="g"></i><i class="w"></i><i class="r"></i></div><a class="btn" href="#">Add to cart</a></article>

<div class="abs partners">
  <span><i></i>Kestrel</span>
  <span><i></i>Halvio</span>
  <span><i></i>Brantwell</span>
  <span><i></i>Olvera</span>
  <span><i></i>Tessmark</span>
  <span><i></i>Kestrel</span>
</div>
<div class="abs partner-dots"><span></span><span class="on"></span></div>

<footer>
  <div class="abs site-footer"></div>
  <div class="abs footer-col" style="left:75px">
    <h3>My Account</h3>
    About us<br>Contact us<br>My account<br>Orders history<br>Advanced search
  </div>
  <div class="abs footer-col" style="left:275px">
    <h3>Contact Information</h3>
    <b>Address:</b><br>123 Street Name, City,<br>England<br>
    <b>Phone:</b><br>(123) 456-7890<br>
    <b>Email:</b><br>mail@example.com<br>
    <b>Working Days/Hours:</b><br>Mon - Sun / 9:00AM -<br>8:00PM
  </div>
  <div class="abs footer-col" style="left:572px">
    <h3>Main Features</h3>
    Expert Advice<br>Secure Shopping<br>Free Delivery
  </div>
  <div class="abs footer-col" style="left:796px">
    <h3>Be the First to Know</h3>
    Get all the latest informa-<br>tion on Events,<br>Sales and Offers. Sign up for<br>newsletter today.
  </div>
  <div class="abs newsletter-input">
    <div class="label">Enter your e-mail Address</div>
    <div class="field"></div>
    <a class="btn" href="#">Submit</a>
  </div>

  <div class="abs bottom-bar"></div>
  <div class="abs bottom-brand"><span class="mark"></span>zandrix.eu</div>
  <div class="abs social"><i></i><i></i><i></i><i></i></div>
  <div class="abs cards"><i></i><i></i><i></i></div>
  <div class="abs copyright">©Copyright 2015 by CompanyName. All Rights Reserved.</div>
</footer>

</body>
</html>
```